QVR Corporate Brochure

This is our general corporate overview brochure highlighting the quality management software that we sell.
-Redesign this - no need to keep the style in which it was already in!
-2 page doc (front and back) This should be 8 1/2" x 11" paper
-Designed for mostly electronic viewing
-Must use Publisher to create the document (illustrator or other design formats will not be accepted)
-Content is written

Target Market(s)

Industrial Markets: automotive, aerospace, medical devices
Quality, Manufacturing and Operations personnel

Industry/Entity Type

Electronic

Requirements
Must have
• -Designed in MS Publisher
-Must have continuity with our corporate colors although design latitude is permitted (PMS 5405, 125, 644, 7530, 471)
-2 pages (front and back)
-Designed for electronic viewing although casual printing may be a possibility
-Preferred Font=Calibri
-Social share icons: facebook, linked-in, twitter
Nice to have
• -Show continuity with our papers and articles (example is attached) called Outlook on Precision for 2013
Should not have
• -not designed in any tool besides Publisher

```html
<!DOCTYPE html>
<html lang="en">
<head>
<meta charset="utf-8">
<title>QVR Corporate Brochure</title>
<link href="https://fonts.googleapis.com/css2?family=Carlito:wght@400;700&family=Open+Sans:wght@600;700&display=swap" rel="stylesheet">
<style>
:root{
  --backdrop:#e6e6e6;
  --paper:#ffffff;
  --paper-shade:#f6f6f6;
  --gold:#d6af3c;
  --gold-deep:#c79e2a;
  --gold-light:#e8c863;
  --gold-pale:#e9cf80;
  --navy:#3d5a78;
  --ink:#4a4a4a;
  --ink-soft:#5d5d5d;
  --white:#ffffff;
}
*{box-sizing:border-box;margin:0;padding:0}
html,body{width:1200px;height:800px;overflow:hidden;background:var(--backdrop)}
body{position:relative;font-family:"Carlito",Calibri,sans-serif;color:var(--ink)}
.page{position:absolute;top:110px;width:408px;height:575px;background:var(--paper);box-shadow:0 2px 6px rgba(0,0,0,.18);overflow:hidden}
.page--front{left:166px}
.page--back{left:613px;background:var(--paper-shade)}
.abs{position:absolute}
p{font-size:6.3px;line-height:9.6px;text-align:justify;hyphens:auto;-webkit-hyphens:auto}

/* front */
.front-header{left:0;top:0;width:100%;height:186px;background:linear-gradient(180deg,var(--gold-light),var(--gold) 55%,var(--gold-deep))}
.brand{font-family:"Open Sans",sans-serif;font-weight:700;color:var(--navy);letter-spacing:1px;white-space:nowrap}
.front-brand{right:26px;top:18px;font-size:36px;line-height:40px}
.front-web{right:28px;top:62px;font-size:5.5px;letter-spacing:2px;color:var(--white)}
.front-title{left:24px;top:95px;font-family:"Carlito",Calibri,sans-serif;font-weight:700;font-size:15.5px;line-height:18px;color:var(--white);letter-spacing:.3px;white-space:nowrap}
.front-title .year{color:var(--navy)}
.front-intro{left:24px;top:126px;width:366px;color:var(--white)}
.front-lead{left:24px;top:192px;width:366px;color:var(--ink)}
.wisdom{left:8px;top:270px;width:384px;height:153px;background:var(--gold-pale)}
.wisdom-head{left:0;top:0;width:100%;height:30px;background:var(--gold-light);text-align:center;padding-top:4px;font-family:"Carlito",Calibri,sans-serif;font-weight:400;font-size:9.6px;line-height:11px;color:var(--navy);white-space:nowrap}
.wisdom-col{top:36px;width:172px;color:var(--ink)}
.wisdom-col--a{left:18px}
.wisdom-col--b{left:202px}
.section-head{left:24px;top:428px;font-family:"Carlito",Calibri,sans-serif;font-weight:400;font-size:9px;line-height:11px;letter-spacing:.7px;color:var(--ink);white-space:nowrap}
.front-body{left:24px;top:445px;width:366px;letter-spacing:.4px;color:var(--ink-soft)}
.social-bar{left:0;bottom:0;width:100%;height:27px;display:flex}
.social-bar .cell{flex:1;display:flex;align-items:center;justify-content:center;gap:5px;font-family:"Open Sans",sans-serif;font-weight:600;font-size:6.4px;letter-spacing:.8px;color:var(--ink);white-space:nowrap}
.cell--a{background:var(--gold)}
.cell--b{background:var(--gold-light)}
.dot{width:8px;height:8px;border-radius:50%;background:var(--navy);flex:none}

/* back */
.col{width:114px}
.col--a{left:30px}
.col--b{left:154px}
.beyond{left:0;top:212px;width:148px;height:44px;background:var(--gold);padding:6px 6px 0 30px;font-weight:700;font-size:6.4px;line-height:9px;color:var(--ink)}
.sidebar{left:277px;top:0;width:131px;height:575px}
.sidebar-top{left:0;top:0;width:131px;height:155px;background:var(--gold)}
.side-brand{left:38px;top:16px;font-size:28px;line-height:32px}
.side-web{left:44px;top:48px;font-size:4.5px;letter-spacing:1.6px;color:var(--white)}
.hq{left:10px;top:72px;font-size:6px;font-weight:700;color:var(--white);letter-spacing:.3px;white-space:nowrap}
.address,.contact{right:14px;font-size:6px;line-height:8px;color:var(--white);text-align:right;white-space:nowrap}
.address{top:94px}
.contact{top:120px}
.photo{left:0;width:131px}
.photo--calc{top:162px;height:67px;background:linear-gradient(135deg,#f2f2f2,#9aa4ad)}
.photo--book{top:236px;height:64px;background:linear-gradient(135deg,#d9c9a4,#8a7550)}
.photo--key{top:305px;height:65px;background:linear-gradient(135deg,#5b5f66,#2d73c2 60%,#3a3d42)}
.photo--screens{top:377px;height:64px;background:linear-gradient(135deg,#eef0f2,#6c7f9a 60%,#c6ccd4)}
.band{left:0;width:131px;height:23px;display:flex;align-items:center;justify-content:flex-end;gap:6px;padding-right:10px;font-family:"Open Sans",sans-serif;font-weight:600;font-size:6.4px;letter-spacing:.8px;color:var(--white);white-space:nowrap}
.band--1{top:447px;background:var(--gold)}
.band--2{top:477px;background:var(--gold-deep)}
.band--3{top:508px;background:var(--gold-pale)}
.band--4{top:539px;background:var(--gold-light)}
</style>
</head>
<body>

<section class="page page--front">
  <div class="abs front-header"></div>
  <div class="abs brand front-brand">QVR</div>
  <div class="abs front-web">WWW.QVR.COM</div>
  <h1 class="abs front-title">QUALITY MANAGEMENT SOFTWARE TRENDS IN <span class="year">2013</span></h1>
  <p class="abs front-intro">Since the turn of the millennium, the proliferation of lean quality management and compliance systems has afforded manufacturers a means to soften the negative financial impacts on total cost of quality. However, as the global economy in 2013 continues its tepid recovery, quality management and compliance departments in the manufacturing industry are taking on a more business-critical role. To increase quality and lower production costs in 2013, manufacturers are searching for new strategies to leverage an enterprise-wide quality management and compliance software solution.</p>
  <p class="abs front-lead">In recent years, technological advancements in the capabilities of networking and information systems have all but obsolesced paper-driven quality management systems, which are simultaneously time-consuming and relatively expensive to maintain. As such, quality automation expenses remain as high as 5-8% of total production costs. Furthermore, manufacturers that conduct operations across multiple sites domestically and abroad must contend with the added challenge of coordinating disparate automated quality-management systems. In some instances, a single manufacturing site may still operate several different automated quality-management systems, further compounding the challenges of deploying novel, 21st-century solutions to improve total cost of quality.</p>

  <div class="abs wisdom">
    <h2 class="abs wisdom-head">THE OLD WISDOM: A BASIC COMPARISON OF SOFTWARE INTEGRATION VERSUS<br>DISPARATE AUTOMATED AND PAPER-DRIVEN QUALITY MANAGEMENT SYSTEMS.</h2>
    <p class="abs wisdom-col wisdom-col--a">Despite the obvious advantages of an integrated software solution, many manufacturers continue to resist transitioning to an integrated, state-of-the-art quality management and compliance software platform. The cost of initial investment along with an uncertain ROI gives business decision-makers cause for concern when analyzing the potential viability of novel IT solutions. From a strictly financial perspective, the wide range of software products from which to choose places quality management professionals in a rather delicate position.</p>
    <p class="abs wisdom-col wisdom-col--b">The problem with paper-driven methods for managing quality from an enterprise-wide perspective lies in the manner in which quality management systems have evolved. In one manner of speaking, many legacy quality management systems accommodate the paper-driven method itself, rather than the method accommodating the system. The latest integrated software solutions on the market seek to correct this imbalance by streamlining quality management processes tailored to the unique requirements of the quality system as a whole from an enterprise-wide perspective.</p>
  </div>

  <h2 class="abs section-head">QUALITY MANAGEMENT SOFTWARE TO REDUCE YOUR TOTAL COST OF QUALITY</h2>
  <p class="abs front-body">QVR provides a powerful and proven solution that offers a unique model for integrating quality systems to achieve superior enterprise-wide performance. It allows companies to become more competitive and profitable, and to achieve and maintain compliance, e.g., ISO 9000, TS 16949, AS 9100, ISO 14001, ISO 13485 etc., and registration faster and at a lower cost than other systems. Instead of being built around the specific characteristics of any one of a number of general and/or industry-specific quality standards, the QVR solution is designed around the needs of complex business processes. Time and time again, QVR has empowered clients to become more profitable and competitive. QVR Quality and Compliance – Right the First Time.</p>

  <nav class="abs social-bar" aria-label="Social channels">
    <div class="cell cell--a"><span class="dot"></span>QVRSOFTWARE</div>
    <div class="cell cell--b"><span class="dot"></span>QVRSOFTWARE</div>
    <div class="cell cell--a"><span class="dot"></span>QVR</div>
    <div class="cell cell--b"><span class="dot"></span>QVRSOFTWARE</div>
  </nav>
</section>

<section class="page page--back">
  <p class="abs col col--a" style="top:24px">When manufacturers opt to deploy disparate automation solutions, the challenge of data collection, analysis and management strains the capabilities of obsolete quality systems. Even after implementing new IT solutions to increase efficiency in quality management processes, the issue of interoperability only exacerbates the operational issues at hand. Surely, the evolution of OPC standardization offers a means to facilitate data transmission between disparate manufacturing components, but the problem of system administration from an enterprise-wide perspective persists even after deploying high-priced integrated software solutions.</p>
  <h3 class="abs beyond">Beyond Software Integration in 2013: Quality Management System Trends Facilitated by the QVR Solution</h3>
  <p class="abs col col--a" style="top:267px">Business decision-makers cannot afford to underestimate the human element of implementing new quality management systems. If deployed correctly, manufacturers can potentially achieve substantial ROI from integrated software solutions within one year. The key is to align integrated systems with current business practices by launching proactive training initiatives. Ideally, novel software solutions should be intuitive enough to take advantage of the technological literacy of quality management personnel.</p>
  <p class="abs col col--a" style="top:427px">Mobility is arguably one of the most exciting trends in the latest quality management software platforms such as the QVR solution. With the proliferation of mobile devices, quality management operators are now able to remain up-to-date on real-time data.</p>

  <p class="abs col col--b" style="top:24px">Communication between IT departments, quality operators, disparate manufacturing sites and upper-level personnel can now be streamlined through software platforms that leverage the mobile device phenomenon. Time-sensitive decisions are no longer subject to the inherent inefficiencies of disparate quality management systems as thousands of employees can view and report data in real time.</p>
  <p class="abs col col--b" style="top:156px">By leveraging the pervasiveness of mobile devices in the workplace, manufacturers can potentially lower the cost of data collection and analysis by as much as 75%. Support and data management expenses can drop by up to 50%, achieving total savings in excess of one million dollars in some instances. The nascent development of mobile device integration into quality management systems provides ample opportunity to increase this total savings figure even further.</p>
  <p class="abs col col--b" style="top:306px">The QVR software solution provides a framework to create a custom API tailored to the unique intricacies of existing quality management systems. Manufacturers also have the option to integrate data as an initial load or to update on a scheduled, as-needed basis. The flexibility of the QVR solution even extends to many of the most widely distributed enterprise systems used today.</p>
  <p class="abs col col--b" style="top:423px">Manufacturing industry experts agree that the success of quality management initiatives hinges on the ability of upper-level Management personnel to breed a new quality management culture. Integrated systems that combine intuitive training, mobile device elements and platform flexibility such as the QVR solution can help manufacturers stay ahead of the curve in 2013.</p>

  <aside class="abs sidebar">
    <div class="abs sidebar-top"></div>
    <div class="abs brand side-brand">QVR</div>
    <div class="abs side-web">WWW.QVR.COM</div>
    <div class="abs hq">QVR, INC. HEADQUARTERS</div>
    <div class="abs address">1180 Meridian Park Dr. #210 <svg width="6" height="7" viewBox="0 0 6 7"><path d="M3 0a2.5 2.5 0 0 1 2.5 2.5C5.5 4.3 3 7 3 7S.5 4.3.5 2.5A2.5 2.5 0 0 1 3 0z" fill="#fff"/><circle cx="3" cy="2.5" r="1" fill="#d6af3c"/></svg><br>Lakeview, OH 44190 USA</div>
    <div class="abs contact">(800)555-0142 <svg width="6" height="6" viewBox="0 0 6 6"><path d="M1 0h1.2l.6 1.6-.8.6a3.5 3.5 0 0 0 1.8 1.8l.6-.8L6 3.8V5a1 1 0 0 1-1 1A5 5 0 0 1 0 1a1 1 0 0 1 1-1z" fill="#fff"/></svg><br>(440)555-0187 <svg width="6" height="6" viewBox="0 0 6 6"><rect x=".5" y="1.5" width="5" height="4" fill="#fff"/><rect x="1.5" y=".5" width="3" height="1.5" fill="#fff"/></svg><br>info@qvr.com <svg width="6" height="5" viewBox="0 0 6 5"><rect width="6" height="5" fill="#fff"/><path d="M0 0l3 2.5L6 0" stroke="#d6af3c" stroke-width=".6" fill="none"/></svg></div>
    <div class="abs photo photo--calc" role="img" aria-label="Photo of a calculator, pen and financial charts"></div>
    <div class="abs photo photo--book" role="img" aria-label="Photo of an open book"></div>
    <div class="abs photo photo--key" role="img" aria-label="Photo of a blue keyboard key labelled learn"></div>
    <div class="abs photo photo--screens" role="img" aria-label="Photo of a row of monitors showing media"></div>
    <div class="abs band band--1">QVRSOFTWARE<span class="dot"></span></div>
    <div class="abs band band--2">QVRSOFTWARE<span class="dot"></span></div>
    <div class="abs band band--3">QVRSOFTWARE<span class="dot"></span></div>
    <div class="abs band band--4">QVR<span class="dot"></span></div>
  </aside>
</section>

</body>
</html>
```